FinServices firm business card
Business card design
Project: FinServices firm business card
FinServices firm business card -
Creative Brief
Use specific fonts
Close to logo, but use whatever makes it look better.
Traditional
Ravindra Kohli
Managing Partner
214 Lantern Avenue, 12th Floor Boston, MA 02187
rkohli@dorvenpartners.example
www.dorvenpartners.example
Please suggest options.. as we have multiple offices and would like to highlight other locations (not addresses). Also, we could twitter, etc.. on back page.. please advise what is norm.

```html
<!DOCTYPE html>
<html lang="en">
<head>
<meta charset="utf-8">
<title>Dorven Partners — Stationery Set</title>
<link rel="stylesheet" href="https://fonts.googleapis.com/css2?family=Cinzel:wght@600&family=Open+Sans:wght@400;600&display=swap">
<style>
  :root {
    --navy: #1f3a68;
    --navy-dark: #162b4f;
    --charcoal: #3b3c3f;
    --paper: #ffffff;
    --paper-shade: #eef0f3;
    --ink: #4a4d52;
    --muted: #8a8f96;
    --backdrop: #e6e5e2;
  }
  * { box-sizing: border-box; margin: 0; padding: 0; }
  html, body { width: 1200px; height: 614px; overflow: hidden; }
  body { background: var(--backdrop); font-family: "Open Sans", sans-serif; color: var(--ink); position: relative; }

  .piece { position: absolute; background: var(--paper); box-shadow: 0 2px 6px rgba(0,0,0,.18); overflow: hidden; }

  .logo { display: flex; align-items: center; gap: 6px; color: var(--navy); }
  .logo-dot { width: 22px; height: 22px; border-radius: 50%; background: currentColor; flex: none; }
  .logo-name { font-family: "Cinzel", serif; font-weight: 600; font-size: 13px; line-height: 1.05; letter-spacing: .5px; }
  .logo--light { color: var(--paper); }
  .logo--large .logo-dot { width: 30px; height: 30px; }
  .logo--large .logo-name { font-size: 17px; }

  .faint-disc { position: absolute; border-radius: 50%; background: rgba(31,58,104,.06); }

  /* card backs */
  .card-back { width: 228px; height: 146px; }
  .card-back--charcoal { left: 72px; top: 72px; background: var(--charcoal); }
  .card-back--navy { left: 72px; top: 232px; background: var(--navy); }
  .card-back--white { left: 72px; top: 382px; background: var(--paper); }
  .card-back .logo { position: absolute; left: 92px; top: 70px; }
  .card-back .card-url { position: absolute; left: 92px; top: 108px; font-size: 6px; }
  .card-back--charcoal .card-url, .card-back--navy .card-url { color: rgba(255,255,255,.7); }
  .card-back--white .card-url { color: var(--muted); }

  /* letterhead */
  .letterhead-under { left: 344px; top: 96px; width: 270px; height: 432px; }
  .letterhead { left: 331px; top: 84px; width: 270px; height: 432px; }
  .letterhead .logo { position: absolute; left: 22px; top: 24px; }
  .letterhead-address { position: absolute; right: 20px; top: 22px; font-size: 5.5px; line-height: 1.45; text-align: right; }
  .letterhead .faint-disc { left: 60px; top: 150px; width: 150px; height: 150px; }
  .letterhead-band { position: absolute; left: 0; right: 0; bottom: 22px; height: 7px; background: var(--navy); }
  .letterhead-url { position: absolute; left: 0; right: 0; bottom: 8px; text-align: center; font-size: 6px; color: var(--muted); }

  /* envelopes */
  .envelope { width: 400px; height: 96px; }
  .envelope svg { position: absolute; inset: 0; }
  .envelope--charcoal { left: 637px; top: 62px; }
  .envelope--navy { left: 637px; top: 122px; }
  .envelope--white { left: 690px; top: 172px; width: 347px; }
  .envelope-front { left: 691px; top: 272px; width: 346px; height: 124px; }
  .envelope-front .logo { position: absolute; left: 18px; top: 18px; }
  .envelope-tagline { position: absolute; left: 18px; top: 50px; font-size: 5.5px; color: var(--muted); }
  .envelope-front .faint-disc { right: 40px; top: 10px; width: 100px; height: 100px; }

  /* card fronts */
  .card-front { width: 222px; height: 122px; top: 420px; }
  .card-front--split { left: 691px; }
  .card-front--stacked { left: 926px; }
  .card-band { position: absolute; left: 0; right: 0; bottom: 0; height: 16px; background: var(--navy); color: var(--paper); font-size: 6px; padding: 4px 10px; }
  .card-front--split .logo { position: absolute; left: 10px; top: 24px; flex-direction: column; gap: 4px; text-align: center; }
  .card-divider { position: absolute; left: 84px; top: 14px; width: 1px; height: 80px; background: #c9ccd1; }
  .card-details { position: absolute; left: 94px; top: 16px; font-size: 5.5px; line-height: 1.5; }
  .card-name { font-size: 9px; font-weight: 600; color: var(--navy); line-height: 1.2; }
  .card-title { font-size: 6px; color: var(--muted); margin-bottom: 6px; }
  .card-front--stacked .logo { position: absolute; left: 14px; top: 20px; flex-direction: column; gap: 4px; text-align: center; }
  .card-front--stacked .card-person { position: absolute; right: 12px; top: 14px; text-align: right; }
  .card-front--stacked .card-contact { position: absolute; right: 12px; top: 44px; text-align: right; font-size: 5.5px; line-height: 1.5; }
</style>
</head>
<body>

  <!-- card backs -->
  <div class="piece card-back card-back--charcoal">
    <div class="logo logo--light"><span class="logo-dot"></span><span class="logo-name">DORVEN<br>PARTNERS</span></div>
    <div class="card-url">www.dorvenpartners.example</div>
  </div>
  <div class="piece card-back card-back--navy">
    <div class="logo logo--light"><span class="logo-dot"></span><span class="logo-name">DORVEN<br>PARTNERS</span></div>
    <div class="card-url">www.dorvenpartners.example</div>
  </div>
  <div class="piece card-back card-back--white">
    <div class="logo"><span class="logo-dot"></span><span class="logo-name">DORVEN<br>PARTNERS</span></div>
    <div class="card-url">www.dorvenpartners.example</div>
  </div>

  <!-- letterhead -->
  <div class="piece letterhead-under"></div>
  <div class="piece letterhead">
    <div class="logo logo--large"><span class="logo-dot"></span><span class="logo-name">DORVEN<br>PARTNERS</span></div>
    <div class="letterhead-address">214 Lantern Avenue, 12th Floor<br>Boston, MA 02187<br>Tel +1 617 555 0142<br>Fax +1 617 555 0143</div>
    <div class="faint-disc"></div>
    <div class="letterhead-band"></div>
    <div class="letterhead-url">www.dorvenpartners.example</div>
  </div>

  <!-- envelope backs -->
  <div class="piece envelope envelope--charcoal">
    <svg viewBox="0 0 400 96" preserveAspectRatio="none"><polygon points="0,0 400,0 200,70" fill="var(--charcoal)"/><circle cx="200" cy="38" r="11" fill="var(--paper)"/></svg>
  </div>
  <div class="piece envelope envelope--navy">
    <svg viewBox="0 0 400 96" preserveAspectRatio="none"><polygon points="0,0 400,0 200,70" fill="var(--navy)"/><circle cx="200" cy="38" r="11" fill="var(--paper)"/></svg>
  </div>
  <div class="piece envelope envelope--white">
    <svg viewBox="0 0 347 96" preserveAspectRatio="none"><polygon points="0,0 347,0 174,70" fill="var(--paper-shade)" stroke="#d8dbe0"/><circle cx="174" cy="38" r="11" fill="var(--navy)"/></svg>
  </div>

  <!-- envelope front -->
  <div class="piece envelope-front">
    <div class="faint-disc"></div>
    <div class="logo logo--large"><span class="logo-dot"></span><span class="logo-name">DORVEN<br>PARTNERS</span></div>
    <div class="envelope-tagline">Investment and advisory services since 1998</div>
  </div>

  <!-- card fronts -->
  <div class="piece card-front card-front--split">
    <div class="logo"><span class="logo-dot"></span><span class="logo-name">DORVEN<br>PARTNERS</span></div>
    <div class="card-divider"></div>
    <div class="card-details">
      <div class="card-name">Ravindra Kohli</div>
      <div class="card-title">Managing Partner</div>
      214 Lantern Avenue, 12th Floor<br>Boston, MA 02187<br>Phone +1 617 555 0142<br>Mobile +1 617 555 0188<br>rkohli@dorvenpartners.example
    </div>
    <div class="card-band">www.dorvenpartners.example</div>
  </div>

  <div class="piece card-front card-front--stacked">
    <div class="logo"><span class="logo-dot"></span><span class="logo-name">DORVEN<br>PARTNERS</span></div>
    <div class="card-person">
      <div class="card-name">Ravindra Kohli</div>
      <div class="card-title">Managing Partner</div>
    </div>
    <div class="card-contact">214 Lantern Avenue, 12th Floor<br>Boston, MA 02187<br>Phone +1 617 555 0142<br>Mobile +1 617 555 0188<br>rkohli@dorvenpartners.example</div>
    <div class="card-band">www.dorvenpartners.example</div>
  </div>

</body>
</html>
```